Calvanta Group Real Estate Company business cards

New business card design, we are generally happy with the basic layout of the existing front of business card, (feel free to change) but require a head shot photo on the back side.

http://www.calvanta.com.au/

Attached logos, and existing business card

------------------------------

Target Market(s)

Real estate

Industry/Entity Type

Real Estate

Contact Information for Business Card

Standard size double sided

Font styles to use
Other font styles liked:
• Futura

Requirements
Must have
• Photo head shot on the back side
Nice to have
• yes
Should not have
• No

```html
<!DOCTYPE html>
<html lang="en">
<head>
<meta charset="utf-8">
<title>Calvanta Group – Business Cards</title>
<link href="https://fonts.googleapis.com/css2?family=Arimo:wght@400;700&display=swap" rel="stylesheet">
<style>
  :root {
    --stage: #e8e5e0;
    --brand-purple: #312563;
    --brand-purple-light: #3d3072;
    --accent-orange: #f6a21c;
    --card-white: #ffffff;
    --photo-grey: #dcdcdc;
    --text-font: "Arimo", Arial, sans-serif;
  }
  * { margin: 0; padding: 0; box-sizing: border-box; }
  html, body {
    width: 1200px; height: 1000px; overflow: hidden;
    background: var(--stage);
    font-family: var(--text-font);
  }
  .stage { position: relative; width: 1200px; height: 1000px; }

  .card {
    position: absolute; left: 265px; width: 667px; height: 398px;
    border-radius: 24px; overflow: hidden;
    box-shadow: 0 6px 16px rgba(0,0,0,0.18);
  }
  .card--front { top: 73px; background: var(--brand-purple); color: var(--card-white); }
  .card--back { top: 532px; background: var(--card-white); }

  .front-texture {
    position: absolute; inset: 0;
    background: linear-gradient(135deg, transparent 30%, rgba(255,255,255,0.05) 55%, transparent 80%);
  }

  .front-line { position: absolute; left: 62px; white-space: nowrap; }
  .holder { top: 78px; font-size: 26px; }
  .holder-name { font-weight: 700; }
  .holder-role { font-weight: 400; }
  .company { top: 141px; font-size: 22px; font-weight: 700; }
  .abn { top: 168px; font-size: 17px; }
  .contact { font-size: 20px; }
  .contact .label { color: var(--accent-orange); margin-right: 4px; }
  .contact--mobile { top: 225px; }
  .contact--mobile .value { font-weight: 700; }
  .contact--email { top: 252px; }
  .contact--web { top: 305px; }

  .front-wordmark {
    position: absolute; left: 548px; top: 50px;
    writing-mode: vertical-rl;
    font-size: 62px; font-weight: 400; line-height: 1;
    color: var(--card-white); letter-spacing: -1px;
  }

  .headshot {
    position: absolute; left: 237px; top: 41px; width: 192px; height: 192px;
    border-radius: 50%;
    background: radial-gradient(circle at 50% 40%, #efefef 0%, var(--photo-grey) 60%, #2e3a52 100%);
  }
  .back-wordmark {
    position: absolute; left: 0; right: 0; top: 260px;
    text-align: center;
    font-size: 68px; font-weight: 400; line-height: 1;
    color: var(--brand-purple); letter-spacing: -1px;
  }
</style>
</head>
<body>
<main class="stage">
  <section class="card card--front">
    <div class="front-texture"></div>
    <p class="front-line holder"><span class="holder-name">Daniel Tran</span> <span class="holder-role">| Director</span></p>
    <p class="front-line company">Calvanta Group</p>
    <p class="front-line abn">ABN: 41 628 905 317</p>
    <p class="front-line contact contact--mobile"><span class="label">M:</span> <span class="value">0412 587 306</span></p>
    <p class="front-line contact contact--email"><span class="label">E:</span> <span class="value">daniel.tran@calvanta.com.au</span></p>
    <p class="front-line contact contact--web"><span class="label">W:</span><span class="value">www.calvanta.com.au</span></p>
    <div class="front-wordmark">calvanta</div>
  </section>

  <section class="card card--back">
    <div class="headshot" role="img" aria-label="Head shot photo of the director in a suit"></div>
    <div class="back-wordmark">calvanta</div>
  </section>
</main>
</body>
</html>
```